New start-up venture BrightPlate needs eye-catching, bright, vibrant catering menu design.

BrightPlate is looking for a tri-fold menu design (6 total pages) for our start-up catering business in Southern New Jersey. Designs should be informative, colorful, appealing, and represent the overall BrightPlate concept:

“The vision of BRIGHTPLATE is to provide high quality organic nutrient dense food, juices, and snacks at affordable prices in a positive, fun, and educational environment inspiring a revolution of optimal health and well-being.”

Brightplate is a Revolutionary catering/take-out concept offering a simple, customizable menu for customers who appreciate a modern approach to traditional food but also place a high priority on health, taste, affordability, and convenience.

Brightplate primary market consists of on-the-go health conscious eaters and those with food allergies. They are deliberate about their eating choices, value quality and convenience, and are willing to pay more for those qualities. We provide Real Food for Real People in the rapidly growing segment of the health conscious dining industry.

• The tri-fold (6 total pages) catering menu brochure must include our name and We Are BrightPlate logo that has been attached.
You are free to pick and choose our personal pictures of salads, juices, snacks, etc. which are also attached.
The list of various BrightPlate benefits on the back page of brochure (also added to the uploaded files).
Actual menu items and descriptions (uploaded file section)
Unique, easy to read (legible), fun, and eye-catching font. Please include the following saying, "Real Food for Real People"

Front cover (First page) should be the We Are BrightPlate logo and space for contact information (You can choose to include pictures of various BrightPlate, fruits, and vegetables or choose from our personal pictures that are attached)
Pages 2 through 5 should each include our various menu items - all information has been attached:
(Page 2 - Information/pictures with names and descriptions of the BrightPlates smoothies, Page 3 - Information/pictures on the Fresh organic juices with names and descriptions, Page 4 - Information/pictures on the Zest Loaded Bowls with names and descriptions, Page 5 - Information/pictures on additional packaged and prepared menu items)
Page 6 (Back cover - the attached list of various BrightPlates benefits - maybe a picture of the We Are BrightPlate spinner game - attached file)
• It would be nice for the brochure to incorporate the colors in the BrightPlate seed of life logo and/or greens, oranges (colors of vegetables). Should you come across a stunning photograph that would benefit brochure, we would entertain that idea of including that photo.
• Too much open or empty space.

```html
<!DOCTYPE html>
<html lang="en">
<head>
<meta charset="utf-8">
<title>BrightPlate Catering Menu – Inside Spread</title>
<link rel="stylesheet" href="https://fonts.googleapis.com/css2?family=Arimo:wght@400;700&family=Didact+Gothic&family=Roboto+Condensed:wght@700&display=swap">
<style>
  :root{
    --paper:#ffffff;
    --ink:#1d1d1d;
    --body:#262626;
    --silhouette:#e2e2e2;
    --pink:#e0468f;
    --purple:#8a3fa6;
    --blue:#3a63b8;
    --green:#5fae3c;
    --yellow:#f2c21a;
    --orange:#f08a1c;
  }
  *{margin:0;padding:0;box-sizing:border-box}
  html,body{width:1200px;height:849px;overflow:hidden;background:var(--paper)}
  .spread{position:relative;width:1200px;height:849px;overflow:hidden;background:var(--paper);
    font-family:"Didact Gothic",sans-serif;color:var(--body);font-size:12.2px;line-height:1.32}
  .backdrop{position:absolute;inset:0}
  .photo{position:absolute}
  .panel{position:absolute;top:0;height:849px}
  .panel p{margin-bottom:12px}
  .panel b{font-family:"Arimo",sans-serif;font-weight:700;color:var(--ink)}

  .tagline{font-family:"Didact Gothic",sans-serif;font-size:32px;color:var(--ink);font-weight:400;margin:40px 0 22px;letter-spacing:-.2px}
  .section-title{font-family:"Arimo",sans-serif;font-weight:700;font-size:24px;color:var(--ink);margin-bottom:12px;letter-spacing:-.2px}
  .condensed-title{font-family:"Roboto Condensed",sans-serif;font-weight:700;font-size:25.5px;color:var(--ink);letter-spacing:-.3px}

  .panel--smoothies{left:15px;width:384px}
  .panel--juices{left:414px;width:382px}
  .panel--bowls{left:814px;width:380px}

  .ingredients{position:absolute;top:103px;left:0;width:380px;font-size:12.6px;line-height:20.2px}
  .ingredients h3{font-family:"Arimo",sans-serif;font-weight:700;font-size:12px;color:var(--ink);position:absolute;top:0}
  .ingredients ul{list-style:none;position:absolute;top:37px}
</style>
</head>
<body>
<main class="spread">

  <svg class="backdrop" width="1200" height="849" viewBox="0 0 1200 849" aria-hidden="true">
    <g opacity=".42">
      <ellipse cx="55" cy="735" rx="95" ry="135" fill="var(--pink)"/>
      <ellipse cx="170" cy="730" rx="95" ry="125" fill="var(--purple)"/>
      <ellipse cx="325" cy="745" rx="80" ry="115" fill="var(--blue)"/>
      <ellipse cx="560" cy="740" rx="120" ry="130" fill="var(--green)"/>
      <ellipse cx="715" cy="730" rx="95" ry="125" fill="var(--yellow)"/>
      <ellipse cx="780" cy="800" rx="70" ry="90" fill="var(--orange)"/>
      <ellipse cx="875" cy="730" rx="85" ry="125" fill="var(--purple)"/>
      <ellipse cx="1020" cy="680" rx="80" ry="100" fill="var(--pink)"/>
      <ellipse cx="1110" cy="760" rx="85" ry="120" fill="var(--purple)"/>
    </g>
  </svg>

  <div class="photo" role="img" aria-label="Grey silhouettes of people jumping with joy" style="left:60px;top:20px;width:300px;height:600px;background:radial-gradient(ellipse at 50% 45%,var(--silhouette) 0%,rgba(226,226,226,.45) 45%,rgba(255,255,255,0) 72%)"></div>
  <div class="photo" role="img" aria-label="Berry smoothie in a glass" style="left:302px;top:171px;width:80px;height:88px;background:linear-gradient(160deg,#f4d7e2,#b0245a 70%,#6a1030)"></div>
  <div class="photo" role="img" aria-label="Cups of orange and pink smoothies" style="left:28px;top:475px;width:77px;height:66px;background:radial-gradient(circle,#f6a23a,#f07a6a 60%,rgba(255,255,255,0) 75%)"></div>
  <div class="photo" role="img" aria-label="Row of colourful fresh juices" style="left:642px;top:312px;width:141px;height:84px;background:linear-gradient(90deg,#a0521c,#d8813c,#c94a4a,#8a3a5a,#d6b28a)"></div>
  <div class="photo" role="img" aria-label="Bundle of fresh green asparagus" style="left:900px;top:125px;width:290px;height:250px;background:linear-gradient(140deg,rgba(255,255,255,0) 20%,rgba(140,190,80,.4) 45%,rgba(111,154,58,.45) 60%,rgba(255,255,255,0) 85%)"></div>
  <div class="photo" role="img" aria-label="Bowl of salad surrounded by spices" style="left:932px;top:428px;width:138px;height:110px;background:radial-gradient(circle at 50% 45%,#6e9a3a,#a0512a 55%,#5a3a28)"></div>
  <div class="photo" role="img" aria-label="Pile of chickpeas" style="left:1098px;top:612px;width:100px;height:80px;background:radial-gradient(ellipse,rgba(217,165,90,.8),rgba(192,138,64,.5) 60%,rgba(255,255,255,0) 78%)"></div>

  <section class="panel panel--smoothies">
    <h1 class="tagline">Real Food for Real People</h1>
    <h2 class="section-title">BrightPlates Smoothies:</h2>
    <p>BlendPro frozen fruit plant based protein smoothies:</p>
    <p style="padding-right:95px"><b>Vanilla Vortex</b> – Frozen fruits include strawberries, pineapple, peaches, mango, and blueberries, Vanilla almond milk, Spirulina Vanilla protein powder, and Vanilla Blueberry Meadow granola clusters</p>
    <p><b>Strawberry Tsunami</b> - Frozen fruits include strawberries, pineapple, peaches, mango, and blueberries, vanilla coconut milk, Spirulina Strawberry protein powder, and Oat &amp; Honey Meadow granola clusters</p>
    <p><b>Chocolate Cyclone</b> - Frozen fruits include strawberries, pineapple, peaches, mango, and blueberries, Chocolate almond milk, Spirulina Chocolate protein powder, and Dark Chocolate &amp; Cranberry Meadow granola clusters</p>
    <p><b>Vanilla Chai Clear Blue Sky</b> - Frozen fruits include strawberries, pineapple, peaches, mango, and blueberries, Vanilla almond/ coconut milk blend, Verda Vanilla chai protein powder, and Cinnamon Oat Meadow granola clusters</p>
    <h2 class="section-title" style="margin-top:88px">Build your own Smoothie:</h2>
    <p>Choice of frozen fruits include strawberries, pineapple, peaches, mango, blueberries, kiwi, and grapes.</p>
    <p>Choice of plant based, Non-GMO protein powders include Vanilla, Strawberry, and Chocolate Spirulina, Vanilla and Chocolate Sunrise Raw Protein blend, Vanilla Chai Verda One Nutritional Shake, and Orchard of Life Raw Organic Vanilla Protein</p>
    <p>Choice of non-dairy milk alternatives include Vanilla &amp; Chocolate Almond (Sweetened and Unsweetened), Vanilla coconut milk, Vanilla &amp; Chocolate Rice milk, and Vanilla quinoa milk</p>
    <p>Choice of Meadow Granola Clusters include Vanilla Blueberry Clusters, Dark Chocolate &amp; Cranberry Clusters, Maple Walnut Clusters with Chia &amp; Quinoa, and Peanut butter Whole Grain Clusters.</p>
  </section>

  <section class="panel panel--juices">
    <h2 class="section-title" style="margin-top:44px;margin-bottom:22px">BrightPlates Me Optional Items:</h2>
    <p>Decadent Blend - Chia and Flax Seed with Coconut and Cacoa</p>
    <p><b>Fresh Organic Juices:</b></p>
    <p><b>Awakening</b> – Fresh organic blend of Apples, Carrots, and Celery</p>
    <p><b>Illuminator</b> – Fresh organic blend of Apples, Carrots, Celery, and Kale</p>
    <p><b>Enlightenment</b> – Fresh organic blend of Apples, Carrots, and Beets</p>
    <p><b>Ascension</b> - Fresh organic blend of Apples, Carrots, Celery, Lemon, and Ginger root</p>
    <p><b>Longevity</b> – Fresh organic blend of Apples, Carrots, Greens, and Harvest Hill Goji Red</p>
    <p style="font-size:12px"><b>BrightPlates-Me Optional Items</b>:<br>Aloe Vera water<br>Chia seeds<br>Spirulina<br>Harvest Hill Red Goji Berry blend</p>
    <h2 class="section-title" style="margin-top:20px;font-size:25px">Zest Loaded Bowls:</h2>
    <p><b>Salad 1: Carb Buster</b> - Dark leafy greens mix AKA:"secret stock", asparagus, green beans, broccoli, cauliflower, green apple, spinach, peppers, cucumber, citrus zest, lemon splash and nuts.</p>
    <p><b>Salad 2: Fruit Delight</b> - Dark leafy greens mix, diced mango, berry assortment, sprouts, carrots, organic raisins or craisins (customer choice).</p>
    <p><b>Salad 3: Mental Clarity/ Energizer</b> - Spinach, Bok Choy, tri-colored bell peppers, beets, blue berries, cabbage duo, orange slices, jicama and sweet potato wedges. Served with savory smooth Turmeric dressing.* Turmeric promotes brain cell stimulation.</p>
    <p><b>Salad 4: The Diabetic's Friend</b> - Dark leafy greens mix, broccoli, cabbage, cauliflower, tomato, avocado, cucumber, onion, spinach, watercress greens, flax, pumpkin and sunflower seeds, beans, nuts and herbs:(cilantro,oregano,basil,mint mixture). This specialty Zest Loaded Bowl comes with a side topping of cinnamon sprinkled apples with museli granola.</p>
    <p><b>Salad 5: Massaged Kale Protein Booster</b> - Kale, edamanme(soy beans), chick peas, finely chopped green beans, dried cherries, sliced almonds, celery leaves, parsley, black beans. This beauty of goodness served on a layer of spinach leaves.</p>
  </section>

  <section class="panel panel--bowls">
    <h2 class="condensed-title" style="margin-top:38px">Build Your Own Zest Loaded Bowl:</h2>
    <div class="ingredients">
      <h3 style="left:0">Base Ingredients:</h3>
      <h3 style="left:274px">Dry Ingredients:</h3>
      <ul style="left:0"><li>Asparagus</li><li>Arugula</li><li>Avocado</li><li>Beets</li><li>Blueberries</li><li>Broccoli</li><li>Carrots</li><li>Jicama</li><li>Kale</li></ul>
      <ul style="left:118px"><li>Mushrooms</li><li>Olives</li><li>Onions</li><li>Radishes</li><li>Romaine</li><li>Spinach</li><li>Sprouts</li><li>Tomatoes</li><li>Watercress greens</li></ul>
      <ul style="left:274px"><li>Chia Seeds</li><li>Craisins</li><li>Ground Flax</li><li>Goji Berries</li><li>Hemp Seeds</li><li>Pumpkin Seeds</li><li>Sunflower Seeds</li><li>Walnut</li><li>Pecans</li><li>Almonds</li></ul>
    </div>
    <p style="position:absolute;top:381px;left:0;width:380px;font-size:12.6px">Choice of salad dressings: Balsamic Vinaigrette, Vidalia onion, Ranch</p>
    <h2 class="condensed-title" style="position:absolute;top:566px;left:0;white-space:nowrap">Additional Packaged Menu Items:</h2>
    <p style="position:absolute;top:604px;left:0;font-size:12.6px;line-height:16.2px">Meadow Bars and Granola Cereals<br>BrightPlates Cereals<br>Wholly Good Multi-Grain and Sweet Potato Chips<br>Early June Sea Salt and Sunny Day Blues Chips<br>Greens Daily Greens and Chocolate Energy Bars<br>Far North Nut Clusters</p>
    <h2 class="condensed-title" style="position:absolute;top:710px;left:0;white-space:nowrap">Additional Prepared Menu Items:</h2>
    <p style="position:absolute;top:750px;left:0;width:380px;font-size:12.6px;line-height:16.2px">Quinoa with Zucchini and Squash. Prepared in olive oil, with pepperoncini and various spices<br>Lean ground Turkey meat quinoa tacos. Prepared in olive oil with pepperoncini and various spices</p>
  </section>

</main>
</body>
</html>
```